Copperleaf Haven Website

Here is the link for all the details, images and information you may need about our website:

https://www.filevaultora.net/s/8kq2mz7rt4wp/NIGEL%20HAMMOND.rar?dl=0

Here is a reference on our competitor: http://www.wanderquill.com.au/ and we want as good as this one.

Number of Pages Required

1 page

```html
<!DOCTYPE html>
<html lang="en">
<head>
<meta charset="utf-8">
<title>Copperleaf Haven Tours – Cape Tribulation and Cairns</title>
<link href="https://fonts.googleapis.com/css2?family=Bangers&family=Exo+2:ital,wght@1,600&family=Quicksand:wght@500;700&family=Rye&family=Tinos:wght@700&display=swap" rel="stylesheet">
<style>
:root{
  --bg:#22130a;
  --panel:#6c3a13;
  --panel-edge:#3e2009;
  --panel-dark:#4a2710;
  --orange:#f29a22;
  --gold:#f3c24a;
  --cream:#f6e6b0;
  --text:#ece3d4;
  --pink:#ef6a8c;
  --link:#6fb3e6;
  --btn-top:#c97a2c;
  --btn-bot:#7d4512;
  --grey-top:#b9b9b9;
  --grey-bot:#6d6d6d;
  --parch:#d9a45c;
}
*{margin:0;padding:0;box-sizing:border-box}
html,body{width:1200px;height:2278px;overflow:hidden;background:var(--bg)}
body{position:relative;font-family:"Quicksand",sans-serif;color:var(--text)}
.abs{position:absolute}
.photo{position:absolute;display:block}

/* header */
.brand{left:22px;top:195px;width:420px;display:flex;align-items:center;gap:12px}
.brand-dot{width:30px;height:30px;border-radius:50%;background:var(--orange);flex:none}
.brand-name{font:700 40px/1 "Quicksand",sans-serif;color:#fff;white-space:nowrap}
.site-title{left:443px;top:78px;width:720px;font:400 64px/1 "Bangers",sans-serif;letter-spacing:3px;color:var(--orange);text-shadow:0 3px 0 #5a2c06;white-space:nowrap}
.nav-btn{position:absolute;height:46px;display:flex;align-items:center;justify-content:center;white-space:nowrap;background:linear-gradient(var(--btn-top),var(--btn-bot));border:2px solid #3b1e06;box-shadow:inset 0 0 0 2px #e2a45a55;font:italic 600 15px/1 "Exo 2",sans-serif;color:#2a1404;letter-spacing:-.4px}

/* hero */
.hero{left:21px;top:283px;width:1152px;height:382px;background:var(--panel-edge)}
.hero-intro{left:28px;top:289px;width:416px;height:370px;background:var(--panel)}
.hero-heading{left:40px;top:352px;width:390px;text-align:center;font:700 24px/1.3 "Quicksand",sans-serif;color:var(--cream)}
.price-sign{left:8px;top:442px;width:222px;height:140px}
.price-text{left:20px;top:462px;width:200px;text-align:center;font:400 21px/1.2 "Rye",serif;color:var(--pink);transform:rotate(-6deg)}
.hero-copy{left:243px;top:424px;width:198px;font:500 13.5px/1.3 "Quicksand",sans-serif;color:#fff}
.btn-grey{position:absolute;display:flex;align-items:center;justify-content:center;white-space:nowrap;background:linear-gradient(var(--grey-top),var(--grey-bot));border:2px solid #4a4a4a;border-radius:6px;font:700 19px/1 "Tinos",serif;color:#fff;text-shadow:0 1px 1px #000}
.slide-caption{left:445px;top:535px;width:542px;height:121px;background:rgba(20,14,10,.72)}
.caption-title{left:485px;top:545px;font:400 34px/1 "Bangers",sans-serif;letter-spacing:1px;color:#fff}
.caption-text{left:488px;top:586px;width:480px;font:500 18px/1.3 "Quicksand",sans-serif;color:#fff;text-indent:36px}
.slide-arrow{position:absolute;top:413px;width:46px;height:112px;background:rgba(120,120,120,.55)}

/* signs */
.sign{position:absolute;font:400 21px/1.15 "Rye",serif;color:var(--pink);text-align:center}

/* inclusions */
.section-heading{position:absolute;font:400 30px/1 "Rye",serif;color:var(--gold);text-shadow:0 2px 0 #4a2206;white-space:nowrap}
.thumb{position:absolute;top:744px;width:93px;height:96px}
.inclusions{left:18px;top:852px;width:720px;list-style:none}
.inclusion{height:108.3px;display:flex;gap:16px}
.inclusion .photo{position:static;width:94px;height:94px;flex:none}
.inclusion div{width:600px}
.inclusion h3{font:italic 700 17px/1 "Quicksand",sans-serif;color:var(--orange);margin:12px 0 4px}
.inclusion p{font:500 17.5px/1.3 "Quicksand",sans-serif;letter-spacing:.5px;color:var(--text);text-indent:38px;padding-left:4px}

/* sidebar */
.sidebar{left:734px;top:893px;width:439px;height:1029px;background:var(--panel);border:3px solid var(--panel-edge)}
.calendar{left:782px;top:972px;width:350px;height:228px;background:var(--parch);border-radius:10px;box-shadow:inset 0 0 18px #8a5518}
.cal-month{left:782px;top:984px;width:350px;text-align:center;font:400 26px/1 "Tinos",serif;color:#6a3a0c}
.cal-grid{left:811px;top:1024px;width:300px;display:grid;grid-template-columns:repeat(7,1fr);row-gap:8px;text-align:center;font:500 18px/1 "Quicksand",sans-serif;color:#fff7e0}
.cal-grid .dow{font-size:13px;color:#fff}
.cal-grid .booked{display:flex;justify-content:center;align-items:center}
.deco{position:absolute}
.gallery{left:753px;top:1341px;width:397px;height:140px;background:var(--panel-dark)}
.gallery .photo{top:6px;width:122px;height:128px}
.testimonials{left:744px;top:1613px;width:416px;height:289px;background:var(--panel-dark);border-radius:8px}
.quote{position:absolute;left:760px;width:390px;display:flex;gap:10px}
.quote svg{flex:none}
.quote p{font:500 15px/1.3 "Quicksand",sans-serif;color:#fff}

/* footer */
.footer-band{left:200px;top:2140px;width:800px;height:60px;background:radial-gradient(ellipse at center,#3a2210 0%,rgba(34,19,10,0) 70%)}
.footer-nav{left:0;top:2164px;width:1184px;display:flex;justify-content:center;gap:16px;font:500 17px/1 "Quicksand",sans-serif;color:var(--link)}
.footer-nav .sep{color:#6a4a30}
.copyright{left:0;top:2202px;width:1184px;text-align:center;font:500 16.5px/1 "Quicksand",sans-serif;color:#fff}
</style>
</head>
<body>

<header>
  <div class="abs photo" role="img" aria-label="Rainforest leaves and butterflies around the brand name" style="left:14px;top:20px;width:440px;height:130px;background:radial-gradient(ellipse at 45% 70%,#2f6b24 0%,#1d3d14 45%,rgba(34,19,10,0) 75%)"></div>
  <div class="abs brand"><span class="brand-dot"></span><span class="brand-name">Copperleaf Haven</span></div>
  <h1 class="abs site-title">CAPE TRIBULATION AND CAIRNS</h1>
  <nav>
    <a class="nav-btn" style="left:497px;top:164px;width:136px">HOME</a>
    <a class="nav-btn" style="left:653px;top:164px;width:137px">ACCOMODATION</a>
    <a class="nav-btn" style="left:811px;top:164px;width:138px">BOOK ONLINE</a>
    <a class="nav-btn" style="left:969px;top:164px;width:140px">CONTACT US</a>
    <a class="nav-btn" style="left:647px;top:225px;width:307px">AUTHENTIC ABORIGINAL ART FOR SALE</a>
  </nav>
</header>

<section class="hero-block">
  <div class="abs hero"></div>
  <div class="abs hero-intro"></div>
  <h2 class="abs hero-heading">A taste of true authentic<br>Aboriginal Culture</h2>
  <div class="abs price-sign photo" role="img" aria-label="Wooden price sign" style="background:linear-gradient(160deg,#c98a3e,#8a5520);border-radius:10px;transform:rotate(-6deg)"></div>
  <p class="abs price-text">ONLY $249<br>TWO DAYS &amp;<br>ONE NIGHT</p>
  <p class="abs hero-copy">Experience true local Indigenous Culture. By twilight traditional Aboriginal food cooking methods and taste testing, demonstration spear and Boomerang throwing! Didjeereedoo playing lessons by a bon fire, dream time stories under the stars!</p>
  <a class="btn-grey" style="left:292px;top:601px;width:142px;height:49px">Read more</a>

  <div class="photo" role="img" aria-label="Crocodiles on a river bank and a fallen log" style="left:445px;top:289px;width:728px;height:367px;background:linear-gradient(90deg,#1d2a16 0%,#4b5a3e 40%,#7a7d70 65%,#5b5a4e 100%)"></div>
  <span class="slide-arrow" style="left:445px"></span>
  <span class="slide-arrow" style="left:1127px"></span>
  <svg class="abs" style="left:458px;top:440px" width="20" height="58" viewBox="0 0 20 58"><path d="M16 2 L4 29 L16 56" fill="none" stroke="#ddd" stroke-width="3"/></svg>
  <svg class="abs" style="left:1141px;top:440px" width="20" height="58" viewBox="0 0 20 58"><path d="M4 2 L16 29 L4 56" fill="none" stroke="#ddd" stroke-width="3"/></svg>
  <div class="abs slide-caption"></div>
  <h3 class="abs caption-title">CROCODILE SIGHTING</h3>
  <p class="abs caption-text">Sight sseeing Crocodiles, bird life, and extensive marine life existing in the river!</p>
</section>

<section class="inclusions-block">
  <h2 class="section-heading" style="left:196px;top:690px">TOUR INCLUSIONS</h2>
  <span class="thumb photo" role="img" aria-label="Crocodile on a log" style="left:152px;background:linear-gradient(#5e6650,#3a3c30)"></span>
  <span class="thumb photo" role="img" aria-label="Crocodile with open jaws" style="left:260px;background:linear-gradient(#1a2a18,#54604a)"></span>
  <span class="thumb photo" role="img" aria-label="Kingfisher bird" style="left:369px;background:linear-gradient(#b9c2b4,#4a6a90)"></span>
  <span class="thumb photo" role="img" aria-label="Green tree frog on a flower" style="left:480px;background:linear-gradient(#2f6a24,#c3462a)"></span>

  <div class="photo" role="img" aria-label="Wooden signposts in grass with hiking boots and a backpack" style="left:714px;top:760px;width:470px;height:136px;background:linear-gradient(#22130a 0%,#5a3a1a 50%,#3c6a22 100%)"></div>
  <div class="photo" role="img" aria-label="Wooden sign" style="left:670px;top:703px;width:226px;height:100px;background:linear-gradient(#d39a50,#9a6126);border-radius:10px;transform:rotate(-5deg)"></div>
  <p class="sign" style="left:676px;top:722px;width:214px;transform:rotate(-5deg)">TRUE LOCAL<br>GUIDES !</p>
  <div class="photo" role="img" aria-label="Wooden sign" style="left:888px;top:626px;width:284px;height:140px;background:linear-gradient(#d39a50,#9a6126);border-radius:10px"></div>
  <p class="sign" style="left:890px;top:642px;width:280px">TRAVEL IN A<br>SMALL EXCLUSIVE<br>INTERMIT GROUP<br>13 OR LESS</p>

  <ul class="abs inclusions">
    <li class="inclusion"><span class="photo" role="img" aria-label="Boat on the river" style="background:linear-gradient(#3c6a34,#6e8a74)"></span><div><h3>Crocodile Sighting</h3><p>Jump on board a boat and explore the notorious Croc infested "Daintree River!" Sight seeing Crocodiles, bird life, and extensive marine life existing in the river!</p></div></li>
    <li class="inclusion"><span class="photo" role="img" aria-label="Waterfall in the rainforest" style="background:linear-gradient(#4a5a3a,#a9b0a0)"></span><div><h3>Folk 'Cascading Crystal'</h3><p>Visit Crystal Cascades one of the secrets of North Queensland that &nbsp;locals have kept hidden from visitors. Crystals is a secluded freshwater &nbsp;swimming hole, hidden in a tropical world heritage listed rainforest.</p></div></li>
    <li class="inclusion"><span class="photo" role="img" aria-label="Fishing by the water" style="background:linear-gradient(#5a6a4a,#3a3a2a)"></span><div><h3>Barramudi Catching</h3><p>Experience the thrill and excitement of catching Australia's most iconic prize fighting fish!</p></div></li>
    <li class="inclusion"><span class="photo" role="img" aria-label="Rainforest boardwalk" style="background:linear-gradient(#2e5a26,#6a8a4a)"></span><div><h3>Scenic Lookout</h3><p>Thorton Peak Lookout. Stop and enjoy the view of the oldest low lying Rainforest in the world!</p></div></li>
    <li class="inclusion"><span class="photo" role="img" aria-label="Knife on a wooden board" style="background:linear-gradient(#8a5422,#5a3310)"></span><div><h3>Aboriginal Food Taste Tasting</h3><p>Experience Aboriginal food taste testing and authentic cooking methods on the beach.</p></div></li>
    <li class="inclusion"><span class="photo" role="img" aria-label="Campfire at twilight" style="background:linear-gradient(#2a1a12,#a0521e)"></span><div><h3>Didjeereedo Playing</h3><p>Spend 3 hours with a local Aboriginal guide listening to the amazing sound of a didjeereedoo! Experience a twilight beach bonfire hearing dream time stories under the stars!</p></div></li>
    <li class="inclusion"><span class="photo" role="img" aria-label="Fire at night" style="background:linear-gradient(#2a0e06,#c8501a)"></span><div><h3>Mud Crab Catching</h3><p>Fish off the beach in a small group with local guides!</p></div></li>
    <li class="inclusion"><span class="photo" role="img" aria-label="Rocky mountain river" style="background:linear-gradient(#4a5a3e,#9aa09a)"></span><div><h3>Mossman Gorge</h3><p>Take a refreshing swim in the beautiful Mossman Gorge mountain river!</p></div></li>
    <li class="inclusion"><span class="photo" role="img" aria-label="Coastline from above" style="background:linear-gradient(#4aa0d8,#2a6a8a)"></span><div><h3>Port Douglas</h3><p>Visit the famous and funky touristic town of Port Douglas!</p></div></li>
    <li class="inclusion"><span class="photo" role="img" aria-label="Tropical beach" style="background:linear-gradient(#3a90d0,#c8b890)"></span><div><h3>Ellis Beach</h3><p>Visit the beautiful Ellis beach</p></div></li>
    <li class="inclusion"><span class="photo" role="img" aria-label="Beach with palm trees" style="background:linear-gradient(#5ab0e0,#2a7aa0)"></span><div><h3>Palm Cove</h3><p>Take a brief walk along the spectacular beach of Palm cove! Enjoy the serenity and take beautiful photos!</p></div></li>
    <li class="inclusion"><span class="photo" role="img" aria-label="Wallabies on a grassy field" style="background:linear-gradient(#8ab0c0,#5a7a3a)"></span><div><h3>Wallaby Kangaroo Sightseeing</h3><p>A brief stop to experience a large local Wallaby group at Trinity beach</p></div></li>
  </ul>
</section>

<aside>
  <div class="abs sidebar"></div>
  <h2 class="section-heading" style="left:822px;top:920px;font-size:20px">AVAILABILITY CALENDAR</h2>
  <div class="abs calendar"></div>
  <span class="deco photo" role="img" aria-label="Painted boomerang" style="left:1092px;top:955px;width:50px;height:70px;background:#b5501e;border-radius:40% 60% 30% 70%"></span>
  <span class="deco photo" role="img" aria-label="Painted boomerang" style="left:752px;top:1170px;width:120px;height:40px;background:#b5501e;border-radius:50%;transform:rotate(-15deg)"></span>
  <div class="abs cal-month">
    <svg width="12" height="18" viewBox="0 0 12 18" style="margin-right:30px"><path d="M11 1 L2 9 L11 17Z" fill="#5a2e08"/></svg>June 2015<svg width="12" height="18" viewBox="0 0 12 18" style="margin-left:30px"><path d="M1 1 L10 9 L1 17Z" fill="#5a2e08"/></svg>
  </div>
  <div class="abs cal-grid">
    <span class="dow">Sun</span><span class="dow">Mon</span><span class="dow">Tues</span><span class="dow">Wed</span><span class="dow">Thurs</span><span class="dow">Fri</span><span class="dow">Sat</span>
    <span></span><span>1</span><span>2</span><span>3</span><span>4</span><span class="booked"><svg width="18" height="18" viewBox="0 0 18 18"><path d="M2 2L16 16M16 2L2 16" stroke="#b0201a" stroke-width="4"/></svg></span><span>6</span>
    <span>7</span><span>8</span><span>9</span><span>10</span><span>11</span><span>12</span><span>13</span>
    <span>14</span><span class="booked"><svg width="18" height="18" viewBox="0 0 18 18"><path d="M2 2L16 16M16 2L2 16" stroke="#b0201a" stroke-width="4"/></svg></span><span>16</span><span>17</span><span>18</span><span>19</span><span>20</span>
    <span>21</span><span>22</span><span>23</span><span class="booked"><svg width="18" height="18" viewBox="0 0 18 18"><path d="M2 2L16 16M16 2L2 16" stroke="#b0201a" stroke-width="4"/></svg></span><span>25</span><span>26</span><span>27</span>
    <span>28</span><span>29</span><span>30</span>
  </div>
  <a class="btn-grey" style="left:1027px;top:1223px;width:121px;height:50px">Book Now!</a>

  <h2 class="section-heading" style="left:754px;top:1298px;font-size:21px">CHECK OUT OUR GALLERY</h2>
  <div class="abs gallery">
    <span class="photo" role="img" aria-label="Rainforest boardwalk" style="left:6px;background:linear-gradient(#3a6a2a,#8aa07a)"></span>
    <span class="photo" role="img" aria-label="Kingfisher bird" style="left:137px;background:linear-gradient(#d0d0d0,#2a5a9a)"></span>
    <span class="photo" role="img" aria-label="Lit market stalls at night" style="left:269px;background:linear-gradient(#3a1a0a,#c87a2a)"></span>
  </div>
  <a class="btn-grey" style="left:1030px;top:1504px;width:120px;height:50px">Click here!</a>

  <h2 class="section-heading" style="left:754px;top:1576px;font-size:21px">TESTIMONIALS</h2>
  <div class="abs testimonials"></div>
  <div class="quote" style="top:1632px"><svg width="34" height="34" viewBox="0 0 34 34"><path d="M17 2 C28 8 30 22 17 32 C4 22 6 8 17 2Z" fill="#3a8a2a"/></svg><p>Lorem ipsum dolor sit amet, consectetuer adipiscing elit. Aenean commodo ligula eget dolor. Aenean massa.</p></div>
  <div class="quote" style="top:1700px"><svg width="34" height="34" viewBox="0 0 34 34"><path d="M17 2 C28 8 30 22 17 32 C4 22 6 8 17 2Z" fill="#3a8a2a"/></svg><p>Lorem ipsum dolor sit amet, consectetuer adipiscing elit. Aenean commodo ligula eget dolor. Aenean massa.</p></div>
  <div class="quote" style="top:1768px"><svg width="34" height="34" viewBox="0 0 34 34"><path d="M17 2 C28 8 30 22 17 32 C4 22 6 8 17 2Z" fill="#3a8a2a"/></svg><p>Lorem ipsum dolor sit amet, consectetuer adipiscing elit. Aenean commodo ligula eget dolor. Aenean massa.</p></div>
  <div class="quote" style="top:1837px"><svg width="34" height="34" viewBox="0 0 34 34"><path d="M17 2 C28 8 30 22 17 32 C4 22 6 8 17 2Z" fill="#3a8a2a"/></svg><p>Lorem ipsum dolor sit amet, consectetuer adipiscing elit. Aenean commodo ligula eget dolor. Aenean massa.</p></div>
</aside>

<footer>
  <div class="abs footer-band"></div>
  <nav class="abs footer-nav"><a>Home</a><span class="sep">|</span><a>Accomodation</a><span class="sep">|</span><a>Book Online</a><span class="sep">|</span><a>Contact Us</a></nav>
  <p class="abs copyright">Copyright © 2015. Copperleaf Haven. All Rights Reserve</p>
</footer>

</body>
</html>
```